New Brochures to deliver confidence of our company to our customers

I would like to have new brochure to be used to distribute to our prospective customers besides the power point presentation. I like the powerpoint you did for us and would like to follow the direction that you have set up. I will attach a number of photos for you to include in our brochure for you to choose. I like the brochure to be modern and forward thinking but just practical. The brochure needs to have three languages which are English, Chinese and Japanese. Attaches is the power point that we like.

Target Market(s)

Multinational companies

Industry/Entity Type

Electronics

Colors

Designer to choose colors to be used in the design.

Requirements
Must have
• Feel lively and modern and yet giving people a sense of confidence. Highlighting the automation is important. Can let us know if you want more photos. The brochure will have three languages, namely english, japanese and chinese.

```html
<!DOCTYPE html>
<html lang="en">
<head>
<meta charset="utf-8">
<title>KVR Circuit Works – Brochure Spread</title>
<link rel="stylesheet" href="https://fonts.googleapis.com/css2?family=Montserrat:wght@400;500;700;800&family=Noto+Sans+SC:wght@500&family=Noto+Sans+JP:wght@500&display=swap">
<style>
  :root{
    --bg:#c9c9c9;
    --paper:#f5f6f5;
    --green:#3f7d3c;
    --green-dark:#2d5b45;
    --accent:#7fd63a;
    --ink:#2a3a2c;
    --muted:#6b776d;
    --chip:#e8eae8;
  }
  *{box-sizing:border-box;margin:0;padding:0}
  html,body{width:1200px;height:887px;overflow:hidden}
  body{background:radial-gradient(ellipse at center,#dcdcdc 0%,var(--bg) 70%,#a9a9a9 100%);font-family:"Montserrat",sans-serif;position:relative}
  .spread{position:absolute;left:40px;top:48px;width:1120px;height:790px;display:flex;box-shadow:0 18px 40px rgba(0,0,0,.28)}
  .page{position:relative;width:560px;height:790px;background:var(--paper);overflow:hidden}
  .page--back{border-right:1px solid #dcdedc}
  .shape{position:absolute;left:0;top:0;width:560px;height:790px}
  .photo{position:absolute;left:0;top:0;width:560px;height:790px}

  .photo--machine{
    background:
      radial-gradient(ellipse 120px 90px at 300px 210px,rgba(150,200,150,.55),transparent 70%),
      radial-gradient(ellipse 140px 120px at 500px 190px,rgba(120,125,118,.7),transparent 70%),
      radial-gradient(ellipse 220px 140px at 80px 450px,rgba(90,110,90,.75),transparent 70%),
      linear-gradient(170deg,#8e948c 0%,#c9ccc6 30%,#e1e3de 55%,#b3b8b0 80%,#6f786c 100%);
    clip-path:polygon(0 120px,560px 120px,560px 398px,250px 474px,0 500px);
  }
  .photo--floor{
    background:
      radial-gradient(ellipse 120px 60px at 110px 560px,rgba(170,200,200,.45),transparent 70%),
      linear-gradient(165deg,#3f8584 0%,#2a6466 55%,#173f42 100%);
  }
  .photo--floor-a{clip-path:polygon(0 510px,238px 484px,214px 600px,0 626px)}
  .photo--floor-b{clip-path:polygon(250px 481px,430px 438px,414px 562px,226px 598px);
    background:radial-gradient(ellipse 110px 60px at 330px 520px,rgba(180,210,205,.45),transparent 70%),linear-gradient(165deg,#4d8d8c 0%,#2a6466 60%,#1a4447 100%)}
  .photo--floor-c{clip-path:polygon(442px 435px,560px 406px,560px 540px,426px 560px);
    background:radial-gradient(ellipse 70px 50px at 500px 480px,rgba(180,210,205,.45),transparent 70%),linear-gradient(165deg,#3f8584 0%,#24595b 100%)}
  .photo--line{clip-path:polygon(486px 300px,560px 300px,560px 640px,390px 640px);
    background:radial-gradient(ellipse 80px 90px at 500px 480px,rgba(170,205,200,.4),transparent 70%),linear-gradient(165deg,#3f8584 0%,#1f4f52 100%)}

  .brand{position:absolute;display:flex;flex-direction:column}
  .brand__name{font-weight:800;color:var(--ink);letter-spacing:4px;line-height:1}
  .brand__tag{font-size:8px;font-weight:700;letter-spacing:2px;color:var(--ink);margin-top:6px}

  .page--back .brand{left:40px;top:46px}
  .page--back .brand__name{font-size:60px}
  .about{position:absolute;left:36px;top:190px;width:330px;color:#fff}
  .section-title{font-size:21px;font-weight:500;letter-spacing:.5px;padding-bottom:8px;border-bottom:1px solid rgba(255,255,255,.5);margin-bottom:14px}
  .section-title strong{color:var(--accent);font-weight:800}
  .about p{font-size:10.5px;line-height:1.45;margin-bottom:10px;text-align:justify}
  .contact{position:absolute;left:36px;top:500px;width:300px;color:#fff}
  .contact ul{list-style:none}
  .contact li{display:flex;align-items:center;gap:10px;font-size:12.5px;margin-bottom:7px}
  .contact svg{width:12px;height:12px;flex:none}
  .partners{position:absolute;left:40px;top:662px;display:grid;grid-template-columns:repeat(8,52px);gap:8px}
  .partner{height:26px;border-radius:3px;background:var(--chip);border:1px solid #dfe2df}
  .partner--red{background:#f2dada}
  .partner--blue{background:#dbe3f1}
  .band-bottom{position:absolute;left:0;bottom:0;width:560px;height:36px;background:var(--green)}

  .page--front .brand{left:60px;top:30px}
  .page--front .brand__name{font-size:46px}
  .hotline{position:absolute;right:30px;top:26px;text-align:right;color:var(--ink)}
  .hotline__phone{font-size:22px;font-weight:800;letter-spacing:.5px}
  .hotline__web{font-size:11px;letter-spacing:1.5px}
  .headline{position:absolute;left:0;top:606px;width:560px;text-align:center}
  .headline h1{font-family:"Montserrat",sans-serif;font-weight:800;font-size:26px;color:var(--green);letter-spacing:.5px;line-height:1.1}
  .headline p{font-size:11px;color:var(--muted);line-height:1.4;margin-top:4px}
  .headline .cjk{font-family:"Noto Sans SC","Noto Sans JP",sans-serif;font-size:10.5px;color:var(--green-dark);margin-top:4px;letter-spacing:1px}
  .headline .cjk span+span::before{content:"｜";color:var(--muted);margin:0 6px}
  .footer-web{position:absolute;left:0;top:748px;width:560px;text-align:center;color:#fff;font-size:13px;letter-spacing:2px}
</style>
</head>
<body>
<div class="spread">

  <section class="page page--back">
    <svg class="shape" viewBox="0 0 560 790" aria-hidden="true">
      <polygon points="0,162 470,162 378,640 0,640" fill="var(--green)"/>
      <line x1="36" y1="150" x2="400" y2="150" stroke="var(--accent)" stroke-width="1"/>
    </svg>
    <div class="photo photo--line" role="img" aria-label="Photo of automated PCB production line"></div>

    <div class="brand">
      <span class="brand__name">KVR</span>
      <span class="brand__tag">Printed Circuit Boards is Our Business</span>
    </div>

    <div class="about">
      <h2 class="section-title">ABOUT <strong>KVR</strong></h2>
      <p>Established in 2007, KVR Circuit Works Limited is a Hong Kong company specializing in single and double sized printed circuit boards. Its manufacturing facility is located in a self-owned facility in Tangxia, Dongguan of China which is 50 minutes from Hong Kong.</p>
      <p>Our mission is to become a premium low cost PCB supplier that fully embraces human, social and environmental responsibilities.</p>
      <p>Through our insatiable drive to maximize efficiency, KVR is becoming a highly efficient PCB factory with a capacity of 140,000 sq meter a month.</p>
      <p>PCB is our business and it is through continued automation and innovation that will drive our growth in the next 10 years.</p>
    </div>

    <div class="contact">
      <h2 class="section-title">GET IN <strong>TOUCH</strong></h2>
      <ul>
        <li><svg viewBox="0 0 12 12"><path d="M6 0a4 4 0 0 1 4 4c0 3-4 8-4 8S2 7 2 4a4 4 0 0 1 4-4z" fill="#fff"/><circle cx="6" cy="4" r="1.5" fill="var(--green)"/></svg>Address Goes Here</li>
        <li><svg viewBox="0 0 12 12"><rect x="0" y="2" width="12" height="8" fill="#fff"/><path d="M0 2l6 5 6-5" stroke="var(--green)" fill="none"/></svg>Info@websiteaddress.com.au</li>
        <li><svg viewBox="0 0 12 12"><circle cx="6" cy="6" r="5" fill="none" stroke="#fff" stroke-width="1.4"/><path d="M1 6h10M6 1v10" stroke="#fff"/></svg>www.websiteaddress.com</li>
        <li><svg viewBox="0 0 12 12"><path d="M2 1l2 0 1 3-1.5 1a7 7 0 0 0 3.5 3.5L8 7l3 1v2c0 1-1 1-1 1C5 11 1 7 1 2c0 0 0-1 1-1z" fill="#fff"/></svg>0123 456 789</li>
      </ul>
    </div>

    <div class="partners" aria-label="Customer badges">
      <div class="partner"></div><div class="partner"></div><div class="partner partner--red"></div><div class="partner partner--blue"></div><div class="partner"></div><div class="partner partner--red"></div><div class="partner partner--red"></div><div class="partner partner--blue"></div>
      <div class="partner"></div><div class="partner"></div><div class="partner partner--blue"></div><div class="partner"></div><div class="partner partner--blue"></div><div class="partner partner--red"></div><div class="partner partner--blue"></div><div class="partner"></div>
    </div>
    <div class="band-bottom"></div>
  </section>

  <section class="page page--front">
    <div class="brand">
      <span class="brand__name">KVR</span>
      <span class="brand__tag">Printed Circuit Boards is Our Business</span>
    </div>
    <div class="hotline">
      <div class="hotline__phone">+123 456 7890</div>
      <div class="hotline__web">www.yourwebsite.com</div>
    </div>

    <div class="photo photo--machine" role="img" aria-label="Photo of PCB handling machine loading a fan of boards"></div>
    <div class="photo photo--floor photo--floor-a" role="img" aria-label="Photo of factory floor machinery"></div>
    <div class="photo photo--floor photo--floor-b" role="img" aria-label="Photo of automated assembly equipment"></div>
    <div class="photo photo--floor photo--floor-c" role="img" aria-label="Photo of production line workstations"></div>

    <div class="headline">
      <h1>KVR CIRCUIT WORKS LIMITED</h1>
      <p>A premium low cost PCB manufacturer that fully embraces<br>human, social and environmental responsibilities.</p>
      <p class="cjk"><span lang="zh">KVR电路制品有限公司</span><span lang="ja">KVR回路製作株式会社</span></p>
    </div>

    <svg class="shape" viewBox="0 0 560 790" aria-hidden="true">
      <polygon points="0,720 560,700 560,712 0,732" fill="var(--green)"/>
      <polygon points="0,732 560,712 560,790 0,790" fill="var(--green-dark)"/>
    </svg>
    <div class="footer-web">www.yourwebsite.com</div>
  </section>

</div>
</body>
</html>
```